Veltracore Needs a Poster to Advertise a New Membership Offer

We need a Poster design for Veltracore Fitness Studio.
A first of it's kind membership, The Veltracore Fitness Studio combines the skills of our industry-leading Physiotherapists, Strength Coaches and Massage Therapists into one membership with a tailored plan to guide you through the fundamentals of Movement, Mobility and Recovery.
The concept is loosely based on the professional sports model, where every member of our team works together to produce lasting results for you. The final design should illustrate the bespoke nature of our program in a fun, supportive and professional space.
"Whether your aim is to be the best in the world, or the best in your world – it’s all the same to us."
Brand Guidelines
The poster should be on a black background and use our brand colour, lime green (hexcode #cefa08) as a highlight. Please don't overuse the highlight colour though. Generally, we opt for less bright colours and more of a 'street' look
Target Market(s)
The poster should attract predominantly female members, but should not exclude males. The target age range is 30-40 years female.
Industry/Entity Type
Health And Wellness
Font styles to use
Requirements
Must have
- Must Include
• VFS logo
• Tag line " Building Strong, Mobile, Bulletproof Humans"
• Call to action "Join us"
• Sized to 600(W)x900(H)mm
• Text: "A first of it's kind membership, The Veltracore Fitness Studio combines the skills of our industry-leading Physiotherapists, Strength Coaches and Massage Therapists into one membership with a tailored plan to guide you through the fundamentals of Movement, Mobility and Recovery."
Nice to have
- Ideal Inclusions
• Veltracore logo
• Text "Membership Now Open"
• Web address: veltracore.com.au
Should not have
- Don't Use:
• Too much of the highlight colour
• Cartoon imagery
• Images that are too staged or revealing (clothing). Image should fit our target market of everyday active people, not elite athletes or models.

```html
<!DOCTYPE html>
<html lang="en">
<head>
<meta charset="utf-8">
<title>Veltracore Fitness Studio – Membership Poster</title>
<link href="https://fonts.googleapis.com/css2?family=Rubik:wght@500;700;900&family=Catamaran:wght@400&display=swap" rel="stylesheet">
<style>
  :root {
    --page-bg: #ecebe6;
    --ink: #111111;
    --white: #ffffff;
    --lime: #c2dc1e;
    --band-light: #7da722;
    --band-deep: #5c8418;
    --ring: #b3d313;
  }
  * { margin: 0; padding: 0; box-sizing: border-box; }
  html, body { width: 1200px; height: 840px; overflow: hidden; }
  body { background: var(--page-bg); position: relative; }

  .poster {
    position: absolute;
    left: 333px; top: 20px;
    width: 533px; height: 800px;
    background: var(--white);
    overflow: hidden;
  }
  .poster-art { position: absolute; inset: 0; }

  .brand-name {
    position: absolute; left: 37px; top: 24px;
    font-family: "Rubik", sans-serif; font-weight: 500;
    font-size: 36px; line-height: 1.1; letter-spacing: 0.3px;
    color: var(--white);
  }
  .club-mark {
    position: absolute; left: 403px; top: 40px;
    font-family: "Rubik", sans-serif; font-weight: 700;
    font-size: 52px; line-height: 1;
    color: var(--white);
  }

  .tagline {
    position: absolute; left: 37px; top: 100px;
    font-family: "Rubik", sans-serif; font-weight: 900;
    font-size: 36px; line-height: 36px;
    text-transform: uppercase;
    color: var(--white);
  }
  .tagline .accent { color: var(--lime); }

  .call-to-action {
    position: absolute; left: 28px; top: 530px;
    font-family: "Rubik", sans-serif; font-weight: 900;
    color: var(--ink); text-transform: uppercase;
  }
  .call-to-action .cta-lead { font-size: 15px; line-height: 19px; display: block; }
  .call-to-action .cta-phone { font-size: 20px; line-height: 23px; display: block; }

  .intro {
    position: absolute; left: 34px; top: 634px; width: 466px;
    font-family: "Catamaran", sans-serif; font-weight: 400;
    font-size: 13.6px; line-height: 17.5px;
    text-align: center; color: var(--ink);
  }

  .membership-pill {
    position: absolute; left: 171px; top: 727px;
    width: 170px; height: 21px; border-radius: 11px;
    background: var(--ink); color: var(--lime);
    font-family: "Rubik", sans-serif; font-weight: 500;
    font-size: 11.5px; line-height: 21px;
    text-align: center; text-transform: uppercase;
  }

  .web-address {
    position: absolute; left: 0; right: 0; top: 750px;
    padding-right: 14px;
    text-align: center;
    font-family: "Rubik", sans-serif; font-weight: 500;
    font-size: 24px; color: var(--ink);
  }
</style>
</head>
<body>
  <main class="poster">
    <svg class="poster-art" width="533" height="800" viewBox="0 0 533 800">
      <defs>
        <radialGradient id="heroTone" cx="0.72" cy="0.18" r="0.95">
          <stop offset="0" stop-color="#6b2a22"/>
          <stop offset="0.25" stop-color="#3e2f22"/>
          <stop offset="0.55" stop-color="#2c331c"/>
          <stop offset="0.8" stop-color="#3d4a22"/>
          <stop offset="1" stop-color="#1a1c12"/>
        </radialGradient>
        <linearGradient id="bandTone" x1="0" y1="0" x2="1" y2="1">
          <stop offset="0" stop-color="var(--band-light)"/>
          <stop offset="1" stop-color="var(--band-deep)"/>
        </linearGradient>
        <radialGradient id="rideTone" cx="0.35" cy="0.3" r="0.85">
          <stop offset="0" stop-color="#f0c27a"/>
          <stop offset="0.3" stop-color="#b7803f"/>
          <stop offset="0.55" stop-color="#6e4a2c"/>
          <stop offset="0.8" stop-color="#a88670"/>
          <stop offset="1" stop-color="#d2b4a2"/>
        </radialGradient>
        <radialGradient id="parkTone" cx="0.5" cy="0.2" r="0.9">
          <stop offset="0" stop-color="#dfe9d2"/>
          <stop offset="0.35" stop-color="#8fb65e"/>
          <stop offset="0.7" stop-color="#5f8f2c"/>
          <stop offset="1" stop-color="#8bb84e"/>
        </radialGradient>
        <radialGradient id="studioTone" cx="0.5" cy="0.25" r="0.9">
          <stop offset="0" stop-color="#f1efea"/>
          <stop offset="0.4" stop-color="#c9c2b6"/>
          <stop offset="0.7" stop-color="#5876a4"/>
          <stop offset="1" stop-color="#3c4f74"/>
        </radialGradient>
      </defs>

      <rect class="hero-photo" width="533" height="600" fill="url(#heroTone)" role="img" aria-label="Photo of a person in red sportswear stretching outdoors on grass"/>
      <path class="green-band" d="M0,252 C150,330 360,300 533,270 L533,420 C400,560 200,600 0,598 Z" fill="url(#bandTone)"/>
      <path class="paper-base" d="M0,598 C200,600 400,560 533,420 L533,800 L0,800 Z" fill="var(--white)"/>

      <circle cx="346" cy="419" r="180" fill="var(--ring)"/>
      <circle class="ride-photo" cx="346" cy="419" r="172" fill="url(#rideTone)" role="img" aria-label="Photo of a cyclist riding a mountain bike on a country path at sunset"/>

      <circle cx="119" cy="384" r="108" fill="var(--white)"/>
      <circle class="park-photo" cx="119" cy="384" r="101" fill="url(#parkTone)" role="img" aria-label="Photo of a coach guiding a woman through a hanging exercise in a park"/>

      <circle cx="427" cy="261" r="92" fill="var(--ring)"/>
      <circle class="studio-photo" cx="427" cy="261" r="84" fill="url(#studioTone)" role="img" aria-label="Photo of a man and a woman doing push-ups together in a studio"/>
    </svg>

    <div class="brand-name">veltracore</div>
    <div class="club-mark">VFS</div>

    <h1 class="tagline">
      Building<br>
      <span class="accent">Strong, Mobile,<br>Bulletproof</span><br>
      Humans
    </h1>

    <p class="call-to-action">
      <span class="cta-lead">Join us today</span>
      <span class="cta-phone">Call 9312 4860</span>
    </p>

    <p class="intro">A first of it’s kind membership, The Veltracore Fitness Studio combines the skills of our industry-leading Physiotherapists, Strength Coaches and Massage Therapists into one membership with a tailored plan to guide you through the fundamentals of Movement, Mobility and Recovery.”</p>

    <div class="membership-pill">Membership now open</div>
    <div class="web-address">veltracore.com.au</div>
  </main>
</body>
</html>
```